A golden web-design opportunity

I have created a quick website (www.brintavexgroup.com.au) but I would like to have the website “polished” to look more professional and have a better consistency.

I would like the website to come across as a genuine, professional insight into our business culture but unfortunately my creative skills have reached their limit.

I have attached a media kit PDF so you are better able to establish what are about.
Updates

Hello All! I just wanted to let everyone know that I do not require an ecommerce site! My website is for potential clients to visit, see what we do and get my contact details...

Gathering more feedback

Hello All, I just wanted to let contestants know that there is not a requirement for my team to be mentioned on the website. I cover in person this as part of my presentation with clients. I have uploaded a new Presentation PDF that has this information excluded. Have a good day!

Target Market(s)

Telecommunications professionals; service delivery partners; white collar executives; construction

Industry/Entity Type

Data Communication

Coding

Coded - Design and coding required

Number of Pages Required

3 page

Font styles to use
Other font styles liked:
• Designers discretion

Colors

Designer to choose colors to be used in the design.

Requirements
Must have
• Must be designed so that I can upload it to Plesk, I think that wordpress is preferred.
• - Page:
• - 1 - Full page is a requirement i.e. the website makes full use of the whole screen
• - 2 - Colour scheme must be "muted" and not agressive
• - Links:
• - 1 - All links will work e.g. "E-Mail us" should work
• - 2 - The page identifier ("[LOGO] Home | Brintavex Gruop) will show the Brintavex logo
• - 3 - A link to facebook and linkedin
• - https://www.facebook.com/brintavexgroup
• - https://www.linkedin.com/company/brintavex-group-pty-ltd/
• - 4 - The phone number icon can be clicked on to make a call
• - 5 - The E-Mail icon can be clicked on to send an E-Mail
Nice to have
• Font:
• - 1 - Rounded is preferred
• - 2 - Colour with reference the logo colours (if possible)
Should not have
• Colour:
• - 1 - To much contrast between colours i.e. balck background with white writing
• - 2 - aggressive colour schemes
• - 3 - Names of Brintavex consultants... These guys are also used by my competetion, only martin is required

```html
<!DOCTYPE html>
<html lang="en">
<head>
<meta charset="utf-8">
<title>Home | Brintavex Solutions</title>
<link rel="stylesheet" href="https://fonts.googleapis.com/css2?family=Oswald:wght@400;500;600&family=Open+Sans:wght@400;600;700&display=swap">
<style>
:root{
  --blue:#2aa6dc;
  --blue-dark:#1b8fc2;
  --ink:#1f2a33;
  --text:#5b6570;
  --muted:#8a949c;
  --light:#f2f4f6;
  --line:#dde2e6;
  --footer:#0f1a21;
  --footer-deep:#0a1318;
  --white:#ffffff;
}
*{box-sizing:border-box;margin:0;padding:0}
html,body{width:1200px;height:2928px;overflow:hidden}
body{font-family:"Open Sans",Arial,sans-serif;color:var(--text);background:var(--white);font-size:14px;line-height:1.6;position:relative}
a{color:inherit;text-decoration:none}
h1,h2,h3,h4{font-family:"Oswald","Arial Narrow",sans-serif;color:var(--ink);font-weight:500;text-transform:uppercase;letter-spacing:.5px}

/* header */
.site-header{height:112px;display:flex;align-items:center;padding:0 72px 0 64px;background:var(--white)}
.brand{display:flex;align-items:center;gap:12px}
.brand-dot{width:40px;height:40px;border-radius:50%;background:var(--blue)}
.brand-name{font-family:"Oswald",sans-serif;font-weight:500;font-size:26px;line-height:1;color:var(--blue);letter-spacing:1px}
.main-nav{margin-left:auto;display:flex;gap:34px;font-size:13px;font-weight:600;text-transform:uppercase;color:var(--ink)}
.main-nav a.active{color:var(--blue)}
.phone-pill{margin-left:56px;background:var(--blue);color:var(--white);border-radius:24px;padding:12px 26px;font-weight:700;font-size:16px;display:flex;align-items:center;gap:10px}

/* hero */
.hero{height:488px;position:relative;background:linear-gradient(180deg,#3d4a55 0%,#5f6c76 45%,#2a333b 100%);display:flex;flex-direction:column;align-items:center;justify-content:center;padding-bottom:90px}
.hero-eyebrow{font-family:"Oswald",sans-serif;color:var(--white);font-size:18px;letter-spacing:3px;text-transform:uppercase}
.hero-title{color:var(--white);font-size:52px;letter-spacing:3px;line-height:1.1}

/* process card */
.process-card{position:absolute;left:120px;top:500px;width:952px;height:300px;background:var(--white);box-shadow:0 6px 24px rgba(0,0,0,.12);padding:38px 40px}
.eyebrow{font-family:"Oswald",sans-serif;font-size:15px;color:var(--ink);text-transform:uppercase;letter-spacing:1px;display:flex;align-items:center;gap:12px}
.eyebrow::after{content:"";width:90px;height:2px;background:var(--blue)}
.process-card h2{font-size:34px;margin-top:2px}
.process-grid{display:grid;grid-template-columns:repeat(3,1fr);gap:48px;margin-top:28px}
.process-item h3{color:var(--blue);font-size:16px}
.process-item p{font-size:12px;line-height:1.55;margin:8px 0 16px}
.btn{display:inline-block;background:var(--blue);color:var(--white);border-radius:16px;padding:5px 16px;font-size:11px;font-weight:600}

/* story */
.story{padding-top:262px;text-align:center}
.section-title{font-size:36px;display:inline-block;position:relative;padding-bottom:10px}
.section-title::after{content:"";position:absolute;left:50%;bottom:0;width:60px;height:3px;background:var(--blue);transform:translateX(-50%)}
.story-intro{width:760px;margin:14px auto 0;font-size:13px}
.story-body{display:flex;gap:48px;margin:18px 0 0 128px;text-align:left}
.story-photo{width:292px;height:288px;background:linear-gradient(135deg,#c9d3da,#8a99a5 60%,#4e5c67)}
.values{display:grid;grid-template-columns:repeat(3,200px);gap:44px;padding-top:24px}
.value{text-align:center}
.value svg{width:52px;height:52px}
.value h3{font-size:17px;margin:10px 0 8px}
.value p{font-size:12px;text-align:left;line-height:1.55;margin-bottom:14px}

/* services */
.services{position:absolute;top:1340px;left:0;width:1200px;height:680px;background:var(--blue);color:var(--white);padding:48px 0 0 128px}
.services h2{color:var(--white);font-size:34px}
.services h2::after{content:"";display:block;width:60px;height:3px;background:var(--white);margin-top:6px}
.services p{font-size:13px;width:520px;margin-top:16px;line-height:1.6}
.services h4{color:var(--white);font-size:18px;margin-top:22px}
.service-list{list-style:none;display:grid;grid-template-columns:260px 260px;gap:8px 0;margin-top:14px;font-size:12.5px}
.service-list li{display:flex;align-items:center;gap:10px}
.service-list svg{width:16px;height:16px;flex:none}
.btn-outline{display:inline-block;margin-top:30px;border:1px solid var(--white);color:var(--white);border-radius:4px;padding:14px 26px;font-size:11px;font-weight:700;text-transform:uppercase}
.services-photo{position:absolute;right:40px;top:60px;width:460px;height:560px;background:linear-gradient(160deg,#4a545c,#2b3238 55%,#c9a626 100%)}

/* contact */
.contact{position:absolute;top:2036px;left:0;width:1200px;text-align:center}
.contact-box{display:flex;width:944px;height:350px;margin:44px auto 0;text-align:left;box-shadow:0 2px 14px rgba(0,0,0,.08)}
.connect{flex:1;padding:44px 44px;background:var(--white)}
.connect h3{font-size:19px}
.connect p{font-size:12px;margin-top:14px;width:400px}
.contact-line{display:flex;align-items:center;gap:12px;color:var(--blue);font-weight:700;font-size:17px;margin-top:18px}
.contact-line svg{width:22px;height:22px}
.message{width:432px;background:var(--light);padding:38px 32px}
.message h3{font-size:19px;margin-bottom:18px}
.fields{display:grid;grid-template-columns:1fr 1fr;gap:12px}
.field{height:34px;background:var(--white);border:1px solid var(--line);font-size:11px;color:var(--muted);padding:8px 12px}
.field.full{grid-column:1/3;height:84px}
.submit{display:inline-block;margin-top:16px;background:var(--blue);color:var(--white);font-size:12px;font-weight:700;border-radius:16px;padding:7px 24px}

/* footer */
.site-footer{position:absolute;top:2600px;left:0;width:1200px;height:328px;background:var(--footer);text-align:center;padding-top:48px}
.site-footer .brand{justify-content:center}
.site-footer .brand-name{color:var(--white)}
.footer-nav{display:flex;justify-content:center;gap:28px;margin-top:22px;font-size:12px;font-weight:600;color:var(--white);text-transform:uppercase}
.social{display:flex;justify-content:center;gap:16px;margin-top:26px}
.social a{width:32px;height:32px;border-radius:50%;background:var(--white)}
.footer-bottom{position:absolute;bottom:0;left:0;width:100%;height:60px;background:var(--footer-deep);display:flex;align-items:center;justify-content:space-between;padding:0 64px;font-size:11px;color:#b7c0c6}
</style>
</head>
<body>

<header class="site-header">
  <a class="brand" href="#"><span class="brand-dot"></span><span class="brand-name">BRINTAVEX SOLUTIONS</span></a>
  <nav class="main-nav">
    <a class="active" href="#">Home</a><a href="#story">Our Story</a><a href="#services">Services</a><a href="#contact">Contact Us</a>
  </nav>
  <a class="phone-pill" href="tel:+61400555018">
    <svg width="16" height="16" viewBox="0 0 24 24" fill="#fff"><path d="M6.6 10.8a15 15 0 006.6 6.6l2.2-2.2a1 1 0 011-.25 11.4 11.4 0 003.6.57 1 1 0 011 1V20a1 1 0 01-1 1A17 17 0 013 4a1 1 0 011-1h3.5a1 1 0 011 1c0 1.25.2 2.45.57 3.6a1 1 0 01-.25 1z"/></svg>
    +61 400 555 018</a>
</header>

<section class="hero" role="img" aria-label="Technician holding a network testing device in front of a server rack">
  <span class="hero-eyebrow">Project Delivery</span>
  <h1 class="hero-title">Done Differently</h1>
</section>

<section class="process-card">
  <span class="eyebrow">Innovation</span>
  <h2>Creating Easy to Manage Processes</h2>
  <div class="process-grid">
    <div class="process-item"><h3>Tailored Onboarding</h3><p>When we onboard all of our employees and contractors we ensure they have all of the industry standard certificates.</p><a class="btn" href="#">Read More</a></div>
    <div class="process-item"><h3>In Field Data Capturing</h3><p>Our field crews are supplied with pre loaded tablets that have every app the team needs to get the job done.</p><a class="btn" href="#">Read More</a></div>
    <div class="process-item"><h3>Quality Management</h3><p>When we onboard all of our employees and contractors we ensure they have all of the industry standard certificates.</p><a class="btn" href="#">Read More</a></div>
  </div>
</section>

<section class="story" id="story">
  <h2 class="section-title">Our Story</h2>
  <p class="story-intro">We are an innovative telecommunications services company. We believe technology can truly change project flow, so we are working with Victoria's most respected delivery partners to complete unique projects faster.</p>
  <div class="story-body">
    <div class="story-photo" role="img" aria-label="Business team meeting around a desk in a bright office"></div>
    <div class="values">
      <div class="value">
        <svg viewBox="0 0 52 52" fill="none" stroke="#2aa6dc" stroke-width="3"><path d="M26 10a12 12 0 00-7 21.8V37h14v-5.2A12 12 0 0026 10z"/><path d="M20 42h12M22 46h8M26 2v4M8 20H4M48 20h-4M12 8l3 3M40 8l-3 3"/></svg>
        <h3>Innovation</h3><p>We have worked with app developers to digitalise field based documentation allowing our clients real time access.</p><a class="btn" href="#">Read More</a>
      </div>
      <div class="value">
        <svg viewBox="0 0 52 52" fill="#2aa6dc"><circle cx="16" cy="14" r="6"/><circle cx="36" cy="14" r="6"/><path d="M6 44V30a8 8 0 0116 0v14zM30 44V30a8 8 0 0116 0v14z"/></svg>
        <h3>Collaboration</h3><p>We view ourselves as an extension of our clients. We believe effective collaboration is intrinsically linked.</p><a class="btn" href="#">Read More</a>
      </div>
      <div class="value">
        <svg viewBox="0 0 52 52" fill="none" stroke="#2aa6dc" stroke-width="3" stroke-linejoin="round"><path d="M4 22l10-8 8 4 8-4 8 4 10 4"/><path d="M14 28l8 8a3 3 0 004-4l4 4a3 3 0 004-4l2 2a3 3 0 004-4L32 18"/></svg>
        <h3>Integrity</h3><p>We have worked with app developers to digitalise field based documentation allowing our clients clear oversight.</p><a class="btn" href="#">Read More</a>
      </div>
    </div>
  </div>
</section>

<section class="services" id="services">
  <h2>Our Services</h2>
  <p>Working with Brintavex Solutions enables a single point of contact for your entire project. We have a wide range of specialists and in-house capabilities that allow us to take on full responsibility for projects.</p>
  <p>Working with Brintavex Solutions reduces clients' deployment costs and time to complete the project.</p>
  <h4>Our Services Include:</h4>
  <ul class="service-list">
    <li><svg viewBox="0 0 16 16"><circle cx="8" cy="8" r="7.5" fill="#fff"/><path d="M4.5 8.2l2.3 2.3 4.7-4.8" stroke="#2aa6dc" stroke-width="1.8" fill="none"/></svg>Project Management (Civil/Fibre)</li>
    <li><svg viewBox="0 0 16 16"><circle cx="8" cy="8" r="7.5" fill="#fff"/><path d="M4.5 8.2l2.3 2.3 4.7-4.8" stroke="#2aa6dc" stroke-width="1.8" fill="none"/></svg>Fibre splicing</li>
    <li><svg viewBox="0 0 16 16"><circle cx="8" cy="8" r="7.5" fill="#fff"/><path d="M4.5 8.2l2.3 2.3 4.7-4.8" stroke="#2aa6dc" stroke-width="1.8" fill="none"/></svg>Asbestos removal</li>
    <li><svg viewBox="0 0 16 16"><circle cx="8" cy="8" r="7.5" fill="#fff"/><path d="M4.5 8.2l2.3 2.3 4.7-4.8" stroke="#2aa6dc" stroke-width="1.8" fill="none"/></svg>Copper jointing</li>
    <li><svg viewBox="0 0 16 16"><circle cx="8" cy="8" r="7.5" fill="#fff"/><path d="M4.5 8.2l2.3 2.3 4.7-4.8" stroke="#2aa6dc" stroke-width="1.8" fill="none"/></svg>Pit and pipe installation</li>
    <li><svg viewBox="0 0 16 16"><circle cx="8" cy="8" r="7.5" fill="#fff"/><path d="M4.5 8.2l2.3 2.3 4.7-4.8" stroke="#2aa6dc" stroke-width="1.8" fill="none"/></svg>Fibre integration</li>
    <li><svg viewBox="0 0 16 16"><circle cx="8" cy="8" r="7.5" fill="#fff"/><path d="M4.5 8.2l2.3 2.3 4.7-4.8" stroke="#2aa6dc" stroke-width="1.8" fill="none"/></svg>Cable hauling (Copper &amp; Fibre)</li>
    <li><svg viewBox="0 0 16 16"><circle cx="8" cy="8" r="7.5" fill="#fff"/><path d="M4.5 8.2l2.3 2.3 4.7-4.8" stroke="#2aa6dc" stroke-width="1.8" fill="none"/></svg>Telecommunication rigging</li>
  </ul>
  <p>Brintavex Solutions has a diverse range of skills, experience and capabilities.</p>
  <a class="btn-outline" href="#contact">For More Details Contact Us Today</a>
  <div class="services-photo" role="img" aria-label="Yellow hard hats lined up on a dark work surface"></div>
</section>

<section class="contact" id="contact">
  <h2 class="section-title">Contact Us</h2>
  <div class="contact-box">
    <div class="connect">
      <h3>Connect with Brintavex Solutions</h3>
      <p>Brintavex Solutions understands business and we take pride in helping Victorian businesses meet their goals.</p>
      <p>Let Brintavex Solutions be part of your business's journey, call us today.</p>
      <a class="contact-line" href="tel:+61400555018" style="margin-top:28px"><svg viewBox="0 0 24 24" fill="#2aa6dc"><path d="M6.6 10.8a15 15 0 006.6 6.6l2.2-2.2a1 1 0 011-.25 11.4 11.4 0 003.6.57 1 1 0 011 1V20a1 1 0 01-1 1A17 17 0 013 4a1 1 0 011-1h3.5a1 1 0 011 1c0 1.25.2 2.45.57 3.6a1 1 0 01-.25 1z"/></svg>+61 400 555 018</a>
      <a class="contact-line" href="mailto:info@brintavexgroup.com.au"><svg viewBox="0 0 24 24" fill="#2aa6dc"><path d="M2 5h20v14H2z"/><path d="M2 5l10 8 10-8" stroke="#fff" stroke-width="1.6" fill="none"/></svg>info@brintavexgroup.com.au</a>
    </div>
    <div class="message">
      <h3>Send Your Message</h3>
      <div class="fields">
        <div class="field">Name...</div><div class="field">E-Mail...</div>
        <div class="field">Phone...</div><div class="field">Subject...</div>
        <div class="field full">Message...</div>
      </div>
      <a class="submit" href="mailto:info@brintavexgroup.com.au">Submit</a>
    </div>
  </div>
</section>

<footer class="site-footer">
  <a class="brand" href="#"><span class="brand-dot"></span><span class="brand-name">BRINTAVEX SOLUTIONS</span></a>
  <nav class="footer-nav"><a href="#">Home</a><a href="#story">Our Story</a><a href="#services">Services</a><a href="#contact">Contact Us</a></nav>
  <div class="social">
    <a href="#" aria-label="Social profile 1"></a>
    <a href="#" aria-label="Social profile 2"></a>
    <a href="#" aria-label="Social profile 3"></a>
    <a href="#" aria-label="Social profile 4"></a>
  </div>
  <div class="footer-bottom"><span>©2018 All Right Reserved. Brintavex Solutions</span><span>www.brintavexgroup.com.au</span></div>
</footer>

</body>
</html>
```